Tarvoe Aviation Consultants Business card

I need a business card design for a new aviation company called Tarvoe Aviation Consultants. Our focus is on large airplane end-of-life solutions. This is typically where an airline retires an aircraft and we would oversee the dismantling of the aircraft into the valuable components and parts. The removed parts are then overhauled and reintroduced into the market place.
'Tarvoe' means 'island in the clouds'. I envision an airplane flying into the sunset as it's days are numbered. I am also very keen on our Florida island vibe.
Industry/Entity Type
Aviation
Contact Information for Business Card
Tarvoe Aviation Consultants
End of Life Specialists
Glen Morsk - President
418 SW 27th Ave
Fort Lauderdale, FL 33872
+1 954 555-0183
Logo Text
Requirements
Must have
- airplane
Nice to have
- sunset
- somewhere on the card it would be the definition of 'Tarvoe' - island in the clouds

```html
<!DOCTYPE html>
<html lang="en">
<head>
<meta charset="utf-8">
<title>Tarvoe Aviation Consultants – Business Card</title>
<link rel="stylesheet" href="https://fonts.googleapis.com/css2?family=Michroma&family=Exo+2:wght@400;500&family=Roboto:wght@400&display=swap">
<style>
  :root {
    --backdrop: #1c1c1e;
    --ink-black: #111111;
    --card-white: #f4f4f4;
    --card-grey: #dcdcdc;
    --accent-orange: #f0401f;
    --text-grey: #6d6d6d;
    --rule-grey: #8c8c8c;
    --white: #ffffff;
    --sun-deep: #8a1d0c;
    --sun-mid: #e8561a;
    --sun-light: #f6a43a;
  }
  * { margin: 0; padding: 0; box-sizing: border-box; }
  html, body {
    width: 1200px; height: 1200px; overflow: hidden;
    background: var(--backdrop);
  }
  .sheet {
    position: relative; width: 1200px; height: 1200px;
    display: flex; flex-direction: column; align-items: center; justify-content: center;
    gap: 44px;
  }
  .card {
    position: relative; width: 900px; height: 514px; overflow: hidden;
    box-shadow: 0 12px 30px rgba(0,0,0,.55);
  }

  /* Front side */
  .card-front { background: var(--ink-black); }
  .front-photo {
    position: absolute; top: 0; right: 0; width: 640px; height: 100%;
    background:
      radial-gradient(circle at 62% 60%, #ffe08a 0 2%, var(--sun-light) 12%, transparent 40%),
      linear-gradient(180deg, #6b4a5a 0%, #d98a4a 30%, var(--sun-light) 52%, var(--sun-mid) 64%, var(--sun-deep) 100%);
  }
  .front-fade {
    position: absolute; top: 0; left: 260px; width: 200px; height: 100%;
    background: linear-gradient(90deg, var(--ink-black), rgba(17,17,17,0));
  }
  /* Title block is laid out horizontally, then turned to read bottom-to-top */
  .front-title {
    position: absolute; left: 46px; top: 470px; width: 430px;
    transform-origin: top left; transform: rotate(-90deg);
  }
  .front-title .brand {
    display: block;
    font-family: "Michroma", sans-serif; font-size: 70px; color: var(--white);
    letter-spacing: 1px; line-height: 1;
  }
  .front-title .division {
    display: block;
    font-family: "Exo 2", sans-serif; font-weight: 500; font-size: 29px;
    color: var(--accent-orange); line-height: 1.15; margin-top: 6px;
    padding-bottom: 4px; border-bottom: 1px solid var(--rule-grey);
  }
  .front-title .focus {
    display: block;
    font-family: "Exo 2", sans-serif; font-weight: 400; font-size: 28px;
    color: var(--white); letter-spacing: 1px; line-height: 1.15; margin-top: 4px;
  }

  /* Back side */
  .card-back {
    background: linear-gradient(160deg, var(--card-grey) 0%, var(--card-white) 55%, var(--white) 100%);
  }
  .back-band {
    position: absolute; top: 0; left: 0; width: 100%; height: 150px;
    background: var(--ink-black);
  }
  .holder { position: absolute; left: 110px; top: 56px; }
  .holder .name {
    font-family: "Michroma", sans-serif; font-size: 26px; color: var(--white); letter-spacing: 1px;
  }
  .holder .role {
    font-family: "Exo 2", sans-serif; font-size: 24px; color: var(--accent-orange); letter-spacing: 2px;
    margin-top: 2px;
  }
  .brand-dot {
    position: absolute; left: 656px; top: 66px; width: 172px; height: 172px; border-radius: 50%;
    background: var(--sun-mid); border: 3px solid var(--accent-orange);
  }
  .wordmark {
    position: absolute; right: 60px; top: 258px; width: 420px; text-align: right;
  }
  .wordmark .brand {
    font-family: "Michroma", sans-serif; font-size: 62px; color: var(--ink-black);
    letter-spacing: 3px; line-height: 1;
  }
  .wordmark .division {
    font-family: "Exo 2", sans-serif; font-weight: 500; font-size: 30px; color: var(--accent-orange);
    letter-spacing: 1px; margin-top: 8px; padding-bottom: 4px; border-bottom: 1px solid #b5b5b5;
  }
  .wordmark .meaning {
    font-family: "Michroma", sans-serif; font-size: 20px; color: var(--text-grey);
    letter-spacing: 2px; line-height: 1.5; margin-top: 4px;
  }
  .contact {
    position: absolute; left: 58px; top: 272px;
    font-family: "Roboto", sans-serif; font-size: 19px; color: var(--ink-black); line-height: 1.4;
  }
  .contact .address { margin-bottom: 12px; }
  .contact .row { display: flex; align-items: center; gap: 12px; }
  .contact .icon { width: 24px; height: 24px; flex: none; }
  .back-footer {
    position: absolute; bottom: 0; left: 0; width: 100%; height: 52px;
    background: var(--accent-orange);
    display: flex; align-items: center; justify-content: center; gap: 60px;
    font-family: "Michroma", sans-serif; font-size: 19px; color: var(--white); letter-spacing: 2px;
  }
</style>
</head>
<body>
<main class="sheet">
  <section class="card card-front">
    <div class="front-photo" role="img" aria-label="Photo of an airliner flying over a tropical beach with palm trees at sunset"></div>
    <div class="front-fade"></div>
    <div class="front-title">
      <span class="brand">TARVOE</span>
      <span class="division">AVIATION CONSULTANTS</span>
      <span class="focus">AIRCRAFT END OF LIFE</span>
    </div>
  </section>

  <section class="card card-back">
    <div class="back-band"></div>
    <div class="holder">
      <div class="name">GLEN MORSK</div>
      <div class="role">PRESIDENT</div>
    </div>
    <div class="brand-dot"></div>
    <div class="wordmark">
      <div class="brand">TARVOE</div>
      <div class="division">AVIATION CONSULTANTS</div>
      <div class="meaning">TARVOE - TAR ~ VOH<br>ISLAND IN THE CLOUDS</div>
    </div>
    <div class="contact">
      <div class="address">418 SW 27th Ave<br>Fort Lauderdale, FL 33872</div>
      <div class="row">
        <svg class="icon" viewBox="0 0 24 24" aria-hidden="true">
          <circle cx="12" cy="12" r="12" fill="var(--accent-orange)"/>
          <path d="M8 7.5c0 5 3.5 8.5 8.5 8.5l1-2-2.3-1.2-1 1c-1.6-.6-2.8-1.8-3.4-3.4l1-1L10.6 6.1z" fill="#fff"/>
        </svg>
        <span>+1 954 555-0183</span>
      </div>
      <div class="row">
        <svg class="icon" viewBox="0 0 24 24" aria-hidden="true">
          <circle cx="12" cy="12" r="12" fill="var(--accent-orange)"/>
          <rect x="6" y="8" width="12" height="8" fill="none" stroke="#fff" stroke-width="1.4"/>
          <path d="M6 8l6 5 6-5" fill="none" stroke="#fff" stroke-width="1.4"/>
        </svg>
        <span>glenmorsk@Tarvoe.aero</span>
      </div>
    </div>
    <div class="back-footer">
      <span>AIRCRAFT PART OUTS</span>
      <span>SALES STRATEGIES</span>
    </div>
  </section>
</main>
</body>
</html>
```